Creative CD cover design

I am after a creative CD cover. The name of the album is called 'Driftwood' . I was thinking of having person (seeing the back of their head... looking into either a mirror or something to see the reflection. In the reflection it will have a pic of me playing the guitar. Or it could be a young kid looking into water/lake or something and seeing a reflection of the older self playing guitar. You can use any colours you think will make it look great. I want it to look modern and professional feel to it. The info will be The name of the album and my name - Tavi Rendell. I dont need a back or a inner sleeve as it is just a digital release. I have attached a couple of pics. Also, if you can think of a better idea... then please do that. Im really just after something that looks awesome! Thanks

```html
<!DOCTYPE html>
<html lang="en">
<head>
<meta charset="utf-8">
<title>Driftwood — Tavi Rendell</title>
<link href="https://fonts.googleapis.com/css2?family=Montserrat:wght@300&family=Playfair+Display:wght@800&display=swap" rel="stylesheet">
<style>
  :root {
    --pearl: #ecebf0;
    --silver: #c9c8d2;
    --lavender: #d9d4ec;
    --sand: #d8cdb4;
    --slate: #8e8c96;
    --ink: #3a3a3e;
    --ink-soft: rgba(58, 58, 62, 0.55);
    --photo-shirt: #e4e4ea;
    --photo-jeans: #2c3140;
  }
  html, body {
    margin: 0;
    width: 1200px;
    height: 1200px;
    overflow: hidden;
  }
  .cover {
    position: relative;
    width: 1200px;
    height: 1200px;
    overflow: hidden;
    background:
      radial-gradient(ellipse 420px 260px at 20% 30%, rgba(255,255,255,0.9), transparent 70%),
      radial-gradient(ellipse 360px 300px at 85% 20%, var(--lavender), transparent 70%),
      radial-gradient(ellipse 380px 260px at 80% 75%, var(--sand), transparent 70%),
      radial-gradient(ellipse 320px 280px at 15% 80%, var(--silver), transparent 70%),
      radial-gradient(ellipse 300px 200px at 55% 55%, rgba(255,255,255,0.85), transparent 70%),
      linear-gradient(135deg, var(--pearl), var(--slate) 50%, var(--pearl));
  }
  .artist-name {
    position: absolute;
    top: 62px;
    left: 0;
    width: 100%;
    text-align: center;
    font-family: "Montserrat", sans-serif;
    font-weight: 300;
    font-size: 30px;
    letter-spacing: 0.95em;
    text-indent: 0.95em;
    color: var(--ink);
    margin: 0;
    z-index: 3;
  }
  .guitarist-photo {
    position: absolute;
    left: 360px;
    top: 370px;
    width: 420px;
    height: 830px;
    border-radius: 180px 180px 0 0;
    background: linear-gradient(180deg, var(--photo-shirt) 0%, var(--photo-shirt) 55%, var(--photo-jeans) 62%, var(--photo-jeans) 100%);
    opacity: 0.8;
    z-index: 1;
  }
  .album-title {
    position: absolute;
    top: 250px;
    left: 78px;
    width: 1050px;
    text-align: center;
    z-index: 2;
  }
  .album-title__word,
  .album-title__reflection {
    display: block;
    font-family: "Playfair Display", serif;
    font-weight: 800;
    font-size: 128px;
    line-height: 0.8;
    letter-spacing: 0.02em;
    margin: 0;
  }
  .album-title__word {
    color: var(--ink);
  }
  .album-title__reflection {
    color: var(--ink-soft);
    transform: scaleY(-1);
    margin-top: -6px;
  }
</style>
</head>
<body>
  <main class="cover">
    <p class="artist-name">TAVI RENDELL</p>
    <div class="guitarist-photo" role="img" aria-label="Photo of the guitarist in a white shirt and dark jeans playing an electric guitar"></div>
    <h1 class="album-title">
      <span class="album-title__word">DRIFTWOOD</span>
      <span class="album-title__reflection" aria-hidden="true">DRIFTWOOD</span>
    </h1>
  </main>
</body>
</html>
```